"Sketch Onward Club" Social Art Website Design

I need a design for a website I am building, which will be called Sketch Onward Club. I have attached the selected logo for the site. The site will be about drawing/art, and how art can be used to brighten a stranger's day as a random act of kindness. In real life, people will receive a drawing or piece of art with details for this site on it. They will in turn be able to give a drawing or piece of art to someone else, thus building a 'chain' of people who are related to each other through the drawings they have received. This should create a strong 'social' aspect to the site. There will be areas of the site for seeing other drawings/art that have been submitted, as well as for seeing different statistics (how many drawings have been submitted, where, how people are connected, etc.).

Target Market(s)

No specific target market.

Industry/Entity Type

Building

Coding

Number of Pages Required

1 page

Font styles to use
Sans Serif
Decorative

Requirements
Must have
• Must use the logo supplied.
Nice to have
• Should be colourful and artistic. References to art tools should be primarily around drawing, though painting can also feature. Colour scheme to match the logo would be ideal.

```html
<!DOCTYPE html>
<html lang="en">
<head>
<meta charset="utf-8">
<title>Sketch Onward Club</title>
<link href="https://fonts.googleapis.com/css2?family=Open+Sans:wght@300;400;600;700&display=swap" rel="stylesheet">
<style>
:root{
  --pink:#e6307e;
  --teal:#2fa9c8;
  --green:#8bb84b;
  --btn-green:#7fb342;
  --ink:#555a60;
  --nav:#666b70;
  --dark:#2a2b30;
  --white:#ffffff;
  --land:#f3f7ec;
}
*{margin:0;padding:0;box-sizing:border-box}
html,body{width:782px;height:1200px;overflow:hidden;background:var(--white);font-family:"Open Sans",sans-serif}
.page{position:relative;width:782px;height:1200px}
.abs{position:absolute}

/* header */
.site-header{left:0;top:0;width:782px;height:102px;background:var(--white)}
.brand{left:86px;top:36px;display:flex;align-items:center;gap:8px}
.brand-dot{width:14px;height:14px;border-radius:50%;background:var(--pink)}
.brand-name{font-size:17px;font-weight:600;color:#3a3d42;letter-spacing:.2px}
.search{left:513px;top:21px;width:119px;height:23px;border:1px solid #cfd3d6;font-size:8px;color:#9aa0a5;padding:6px 10px}
.search svg{position:absolute;right:8px;top:6px}
.sign-in{left:642px;top:21px;width:52px;height:23px;background:var(--teal);color:var(--white);font-size:8px;display:flex;align-items:center;justify-content:center;gap:3px}
.main-nav{top:68px;left:0;width:782px;font-size:8px;color:var(--nav)}
.main-nav span{position:absolute;top:0}
.main-nav .active{color:var(--pink)}

/* hero */
.hero{left:0;top:102px;width:782px;height:297px;border-top:2px solid #9fc6c0;
  background:linear-gradient(100deg,#5fc0c6 0%,#e9d48e 30%,#4fb2c2 45%,#d99a3a 65%,#c68a30 80%,#7fb8c4 100%)}
.hero-title{right:88px;top:232px;text-align:right;font-size:21px;font-weight:700;line-height:24px;color:var(--white);text-shadow:0 1px 3px rgba(0,0,0,.45)}
.slider-dots{left:366px;top:376px;width:49px;height:12px;border-radius:6px;background:rgba(40,40,50,.55);display:flex;align-items:center;justify-content:center;gap:4px}
.slider-dots i{width:5px;height:5px;border-radius:50%;background:var(--white)}
.slider-dots i:first-child{background:transparent;border:1px solid var(--white)}

/* welcome */
.welcome{left:86px;top:428px;width:608px;text-align:center}
.welcome h1{font-size:22px;font-weight:300;color:var(--pink);line-height:28px}
.welcome p{margin-top:5px;font-size:7.6px;line-height:14.8px;color:var(--ink)}
.cta{left:339px;top:513px;width:103px;height:31px;background:var(--btn-green);border:1px solid #6c9f35;color:var(--white);font-size:11px;display:flex;align-items:center;justify-content:center}

/* stats */
.stats{left:0;top:583px;width:782px;height:152px;background:linear-gradient(110deg,#3b3e2c 0%,#2c2b25 35%,#4a4433 60%,#2f3134 100%)}
.stat{width:150px;text-align:center;color:var(--white)}
.stat-icon{width:46px;height:46px;margin:0 auto;border:2px solid var(--white);border-radius:50%;display:flex;align-items:center;justify-content:center}
.stat-num{font-size:27px;font-weight:700;line-height:30px;margin-top:12px}
.stat-label{font-size:13px;line-height:16px;margin-top:4px}

/* reach map */
.reach{left:0;top:735px;width:782px;height:209px;background:var(--green)}
.world-map{left:228px;top:20px;width:328px;height:172px;border-radius:22px;
  background:radial-gradient(ellipse at 50% 45%,rgba(255,255,255,.92) 0%,rgba(255,255,255,.75) 55%,rgba(255,255,255,.25) 100%)}
.pins{left:0;top:0}

/* recent */
.recent-title{left:0;top:974px;width:782px;text-align:center;font-size:15px;font-weight:400;color:var(--pink)}
.thumb{top:1010px;width:113px;height:80px}
.pager{top:1108px;left:364px;display:flex;gap:10px}
.pager i{width:5px;height:5px;border-radius:50%;background:#bfc3c6}
.pager i:first-child{background:var(--pink)}

/* footer */
.site-footer{left:0;top:1148px;width:782px;height:52px;background:var(--dark)}
.social{left:86px;top:21px;display:flex;gap:11px}
.social i{width:9px;height:9px;border-radius:50%;background:#8f939a}
.footer-links{right:88px;top:12px;font-size:6.5px;color:#9a9ea5}
.copyright{right:88px;top:29px;font-size:6.5px;color:#9a9ea5}
</style>
</head>
<body>
<div class="page">

  <header class="site-header abs">
    <div class="brand abs"><span class="brand-dot"></span><span class="brand-name">Sketch Onward Club</span></div>
    <div class="search abs">Search
      <svg width="8" height="8" viewBox="0 0 10 10"><circle cx="4" cy="4" r="3" fill="none" stroke="#666" stroke-width="1.4"/><path d="M6.3 6.3 9 9" stroke="#666" stroke-width="1.4"/></svg>
    </div>
    <div class="sign-in abs">
      <svg width="6" height="7" viewBox="0 0 6 7"><rect x="0" y="3" width="6" height="4" fill="#fff"/><path d="M1.3 3V2a1.7 1.7 0 0 1 3.4 0" fill="none" stroke="#fff"/></svg>Sign in
    </div>
    <nav class="main-nav abs">
      <span class="active" style="left:406px">Find a Drawing</span>
      <span style="left:480px">About</span>
      <span style="left:522px">FAQ</span>
      <span style="left:558px">Contact</span>
      <span style="left:606px">Report</span>
      <span style="left:651px">Our Policies</span>
    </nav>
  </header>

  <section class="hero abs" role="img" aria-label="Colourful oil painting of two boats on a lake beside golden reeds"></section>
  <h2 class="hero-title abs">Donec tincidunt sodales<br>nulla ut vulputate</h2>
  <div class="slider-dots abs"><i></i><i></i><i></i><i></i></div>

  <section class="welcome abs">
    <h1>Welcome to Sketch Onward Club</h1>
    <p>We believe that the gift of hand-made art – a simple drawing with a nice message for a stranger – can brighten someone's day and make the world just a little bit better.
    We also believe everyone is an artist, whether or not you've had any training or think you have any artistic talent. We created Sketch Onward Club to join people together through art, creating an artistic chain of smiling people linked together through the simple act of drawing.</p>
  </section>
  <div class="cta abs">Start a Drawing</div>

  <section class="stats abs" role="img" aria-label="Photo of paint brushes and paint tubes on a dark table">
    <div class="stat abs" style="left:87px;top:16px">
      <div class="stat-icon"><svg width="18" height="18" viewBox="0 0 18 18"><circle cx="9" cy="5" r="4" fill="#fff"/><path d="M1 17c0-5 3.5-7 8-7s8 2 8 7z" fill="#fff"/></svg></div>
      <div class="stat-num">18,542</div><div class="stat-label">Users</div>
    </div>
    <div class="stat abs" style="left:239px;top:16px">
      <div class="stat-icon"><svg width="18" height="18" viewBox="0 0 18 18"><path d="M16 1 7 11l1.8 1.8L17 3z" fill="#fff"/><path d="M6 12c-3 0-3 3-5 5 3 0 7 0 7-3z" fill="#fff"/></svg></div>
      <div class="stat-num">1,02,841</div><div class="stat-label">Drawings Submitted</div>
    </div>
    <div class="stat abs" style="left:392px;top:16px">
      <div class="stat-icon"><svg width="22" height="18" viewBox="0 0 22 18"><circle cx="11" cy="5" r="3.5" fill="#fff"/><circle cx="4.5" cy="7" r="2.5" fill="#fff"/><circle cx="17.5" cy="7" r="2.5" fill="#fff"/><path d="M5 17c0-5 2.5-7 6-7s6 2 6 7z" fill="#fff"/><path d="M0 16c0-3 2-5 4.5-5 1 0 1.5.3 2 .6C5 13 4.5 14.5 4.5 16z" fill="#fff"/><path d="M22 16c0-3-2-5-4.5-5-1 0-1.5.3-2 .6 1.5 1.4 2 2.9 2 4.4z" fill="#fff"/></svg></div>
      <div class="stat-num">6,851</div><div class="stat-label">Top Artists</div>
    </div>
    <div class="stat abs" style="left:544px;top:16px">
      <div class="stat-icon"><svg width="18" height="18" viewBox="0 0 18 18"><path d="M13 4 5 9l8 5" fill="none" stroke="#fff" stroke-width="2"/><circle cx="13.5" cy="3.5" r="3" fill="#fff"/><circle cx="4.5" cy="9" r="3" fill="#fff"/><circle cx="13.5" cy="14.5" r="3" fill="#fff"/></svg></div>
      <div class="stat-num">19,012</div><div class="stat-label">Shares</div>
    </div>
  </section>

  <section class="reach abs">
    <div class="world-map abs" role="img" aria-label="White world map showing where drawings were submitted"></div>
    <svg class="pins abs" width="782" height="209" viewBox="0 0 782 209" aria-label="Pink location pins marking drawing submissions">
      <defs>
        <g id="pin">
          <path d="M0 0C-2.5-3.5-5-6-5-9a5 5 0 0 1 10 0c0 3-2.5 5.5-5 9z" fill="#e6307e"/>
          <circle cx="0" cy="-9" r="2" fill="#fff"/>
        </g>
      </defs>
      <use href="#pin" x="338" y="33"/><use href="#pin" x="346" y="51"/>
      <use href="#pin" x="254" y="61"/><use href="#pin" x="278" y="76"/>
      <use href="#pin" x="295" y="75"/><use href="#pin" x="305" y="82"/>
      <use href="#pin" x="377" y="96"/><use href="#pin" x="402" y="93"/>
      <use href="#pin" x="415" y="115"/><use href="#pin" x="420" y="57"/>
      <use href="#pin" x="424" y="67"/><use href="#pin" x="442" y="51"/>
      <use href="#pin" x="474" y="45"/><use href="#pin" x="520" y="43"/>
      <use href="#pin" x="447" y="75"/><use href="#pin" x="466" y="73"/>
      <use href="#pin" x="487" y="69"/><use href="#pin" x="440" y="87"/>
      <use href="#pin" x="445" y="99"/><use href="#pin" x="453" y="101"/>
      <use href="#pin" x="449" y="109"/><use href="#pin" x="483" y="89"/>
      <use href="#pin" x="321" y="135"/><use href="#pin" x="329" y="149"/>
      <use href="#pin" x="317" y="174"/><use href="#pin" x="498" y="147"/>
      <use href="#pin" x="520" y="147"/><use href="#pin" x="525" y="159"/>
    </svg>
  </section>

  <h2 class="recent-title abs">Recently Submitted</h2>
  <div class="thumb abs" style="left:86px;background:linear-gradient(135deg,#d9782f,#2e8fc4)" role="img" aria-label="Painted ancient figures with amphora"></div>
  <div class="thumb abs" style="left:210px;background:linear-gradient(135deg,#f3a23a,#c84ea0,#56b45a)" role="img" aria-label="Bright abstract flower painting"></div>
  <div class="thumb abs" style="left:334px;background:linear-gradient(180deg,#f2f2f4,#d9e6f3 55%,#3d7fd0)" role="img" aria-label="Hand painting blue waves in watercolour"></div>
  <div class="thumb abs" style="left:458px;background:radial-gradient(circle,#c9a75a,#5c4318)" role="img" aria-label="Golden textured abstract canvas"></div>
  <div class="thumb abs" style="left:582px;background:linear-gradient(135deg,#f5f5f5,#e7e7e7)" role="img" aria-label="Watercolour sketch of a small red-breasted bird"></div>
  <div class="pager abs"><i></i><i></i><i></i><i></i></div>

  <footer class="site-footer abs">
    <div class="social abs"><i></i><i></i><i></i><i></i><i></i><i></i></div>
    <div class="footer-links abs">Find a Drawing &nbsp;| &nbsp;About &nbsp;| &nbsp;FAQ &nbsp;| &nbsp;Contact &nbsp;| &nbsp;Report &nbsp;| &nbsp;Our Policies</div>
    <div class="copyright abs">Copyright © 2016 &nbsp;Sketch Onward Club. &nbsp;All rights reserved</div>
  </footer>

</div>
</body>
</html>
```